Infographic for Commercial Painting and Flooring Company

We need an Infographic that shows a compelling argument for signing on with Verimbos for a maintenance contract vs a project. The infographic should be easily understood visually so sell the story we have provided. 1) What does the quick view give me? 2) Am I interested in this? 3) Does this bring me any value? 4) Is this “everything I have seen before or something new and different”? Included here is a word document called Maintenance vs Project Notes with the written content and instructions, a logo, and two other marketing pieces they currently use so you can see how their brand is being used. Colors should be on brand. I'd like to get this done ASAP if possible. We do not want this piece to look busy.

I added two images called Sample 1 and Sample 2 to portray the types of infographics we like. Simple and clear. Love the watch with the pie chart built in....a smaller version of that would be great for us based on the notes document I provided.

Target Market(s)

Facilities Manufacturers and owners of manufacturing facilities

Font styles to use
Sans Serif

Colors

Designer to choose colors to be used in the design.

Requirements
Must have
• Simple, clean, tell a clear story
Nice to have
• Iconography, pie chart, Men in hard hat
Should not have
• Too many colors. Stick with the brand colors and maybe a few others. Don't want it too look to busy.

```html
<!DOCTYPE html>
<html lang="en">
<head>
<meta charset="utf-8">
<title>Verimbos – Maintenance vs Project Infographic</title>
<link rel="stylesheet" href="https://fonts.googleapis.com/css2?family=Roboto+Condensed:wght@400;700&family=Signika:wght@600;700&family=Open+Sans:wght@400;600;700&display=swap">
<style>
  :root{
    --navy:#1a2ba3;
    --blue:#1f45c9;
    --lime:#9cc81a;
    --lime-dark:#7fae12;
    --lime-text:#a3cc1d;
    --grey:#6e6e6e;
    --ink:#2a2a2a;
    --mint-1:#c6f6e8;
    --mint-2:#ecfffa;
    --page:#ffffff;
  }
  *{box-sizing:border-box;margin:0;padding:0}
  html,body{width:1200px;height:850px;overflow:hidden;background:var(--page)}
  body{position:relative;font-family:"Open Sans",sans-serif;color:var(--navy)}

  .panel{position:absolute;background:radial-gradient(ellipse at 50% 45%,var(--mint-2) 0%,var(--mint-1) 100%);overflow:hidden}
  .panel--tall{left:51px;top:49px;width:360px;height:756px}
  .panel--wide{left:433px;top:198px;width:719px;height:453px}

  .brand{position:absolute;display:flex;align-items:center;gap:6px;font-family:"Roboto Condensed",sans-serif;font-weight:700;color:var(--navy);letter-spacing:-.3px}
  .brand__mark{background:var(--lime-dark)}
  .panel--tall .brand{left:122px;top:12px;font-size:22px}
  .panel--tall .brand__mark{width:34px;height:34px}
  .panel--wide .brand{left:16px;top:8px;font-size:30px}
  .panel--wide .brand__mark{width:44px;height:44px}

  /* vendor story block */
  .story{position:absolute;width:320px;height:330px}
  .panel--tall .story{left:22px;top:78px}
  .panel--wide .story{left:12px;top:84px}
  .story__intro-title{position:absolute;left:0;top:0;width:204px;font-family:"Roboto Condensed",sans-serif;font-weight:700;font-size:13px;line-height:17px;color:var(--navy);text-align:justify;text-align-last:justify}
  .story__intro-text{position:absolute;left:0;top:39px;width:210px;font-size:7.2px;line-height:14.5px;color:var(--ink)}
  .story__hero{position:absolute;left:216px;top:-26px;width:104px;height:100px;border-radius:45% 55% 40% 60%/55% 45% 55% 45%;background:linear-gradient(135deg,var(--blue) 0%,#2f6fe0 55%,var(--lime) 100%)}
  .story__headline{position:absolute;left:-4px;top:85px;width:330px;text-align:center;font-family:"Roboto Condensed",sans-serif;font-weight:700;font-size:19.5px;line-height:17px;letter-spacing:-.6px;color:var(--navy)}
  .story__chart{position:absolute;left:42px;top:128px;width:240px;height:120px}
  .story__total{position:absolute;left:0;top:256px;width:320px;text-align:center;font-family:"Roboto Condensed",sans-serif;font-size:14.5px;line-height:15px;color:var(--grey);letter-spacing:-.4px}
  .story__once{position:absolute;left:0;top:294px;width:320px;text-align:center;font-family:"Roboto Condensed",sans-serif;font-weight:700;font-size:17px;line-height:17px;color:var(--navy);letter-spacing:-.5px}
  .accent{color:var(--lime-text)}

  .chart-label{font-family:"Open Sans",sans-serif;font-weight:700;font-size:8.5px;fill:var(--navy)}
  .chart-value{font-family:"Open Sans",sans-serif;font-weight:700;font-size:14px;fill:#fff}

  /* solution block */
  .solution{position:absolute;text-align:center}
  .panel--tall .solution{left:0;top:415px;width:360px}
  .panel--wide .solution{left:360px;top:26px;width:340px}
  .solution__title{font-family:"Signika",sans-serif;font-weight:700;color:var(--lime-text)}
  .solution__subtitle{font-family:"Roboto Condensed",sans-serif;font-weight:700;color:var(--navy)}
  .solution__lead{font-family:"Roboto Condensed",sans-serif;color:var(--ink)}
  .panel--tall .solution__title{font-size:25px;line-height:25px}
  .panel--tall .solution__subtitle{font-size:11.5px;line-height:12px}
  .panel--tall .solution__lead{font-size:8.5px;line-height:11px;margin:1px 0 0 60px}
  .panel--wide .solution__title{font-size:30px;line-height:32px}
  .panel--wide .solution__subtitle{font-size:13.5px;line-height:15px}
  .panel--wide .solution__lead{font-size:13px;line-height:16px;margin-top:14px}

  .benefits{display:flex;justify-content:space-between}
  .panel--tall .benefits{margin:6px 18px 0 20px}
  .panel--wide .benefits{margin:12px 0 0 14px}
  .benefit{display:flex;flex-direction:column;align-items:center}
  .benefit__art{border-radius:50% 42% 55% 45%/45% 55% 45% 55%;background:radial-gradient(circle at 40% 40%,#b6dc3a,var(--lime-dark))}
  .benefit__text{font-family:"Open Sans",sans-serif;font-weight:700;color:var(--navy);margin-top:4px}
  .panel--tall .benefit{width:104px}
  .panel--tall .benefit__art{width:66px;height:62px}
  .panel--tall .benefit__text{font-size:7.2px;line-height:9.6px}
  .panel--wide .benefit{width:108px}
  .panel--wide .benefit__art{width:68px;height:66px}
  .panel--wide .benefit__text{font-size:8px;line-height:10px}

  .partner__title{font-family:"Roboto Condensed",sans-serif;font-weight:700;color:var(--navy);letter-spacing:-.2px}
  .panel--tall .partner__title{font-size:16px;line-height:18px;margin-top:14px}
  .panel--wide .partner__title{font-size:16.5px;line-height:19px;margin-top:20px}
  .pills{display:flex;justify-content:space-between;list-style:none}
  .panel--tall .pills{margin:8px 22px 0 16px}
  .panel--wide .pills{margin:9px 8px 0 9px}
  .pill{width:103px;height:18px;border-radius:9px;background:linear-gradient(90deg,#b3d92c,var(--lime) 60%,var(--lime-dark));font-family:"Signika",sans-serif;font-weight:600;font-size:12.5px;line-height:18px;color:#fff}
  .aligned{font-family:"Roboto Condensed",sans-serif;font-weight:700;color:var(--navy)}
  .panel--tall .aligned{font-size:11.5px;line-height:14px;margin-top:3px}
  .panel--wide .aligned{font-size:11.5px;line-height:14px;margin-top:10px}
  .divider{height:1px;background:linear-gradient(90deg,transparent,#8fb7c8,transparent);margin:9px 30px 0}
  .features{list-style:none;font-family:"Open Sans",sans-serif;font-weight:600;letter-spacing:-.2px}
  .features li:nth-child(odd){color:var(--navy)}
  .features li:nth-child(even){color:var(--lime-text)}
  .panel--tall .features{font-size:7.6px;line-height:10.3px;margin-top:6px}
  .panel--wide .features{font-size:9.6px;line-height:13.8px;margin-top:6px;margin-left:-30px;margin-right:-30px}
</style>
</head>
<body>

<!-- Portrait version -->
<section class="panel panel--tall">
  <div class="brand"><span class="brand__mark"></span>Verimbos</div>

  <div class="story">
    <h2 class="story__intro-title">Imagine What You Could Do with<br>An Extra 30% More Time Each Year?</h2>
    <p class="story__intro-text">Time that you wouldn't need to spend on-boarding a new company every time you have a project or facility upgrade.</p>
    <div class="story__hero" role="img" aria-label="Illustration of a worker in a hard hat thinking, with question marks"></div>
    <h1 class="story__headline">It Takes <span class="accent">30+ Hours</span> to Source and Onboard the Most Qualified Vendor...<span class="accent">YIKES!</span></h1>
    <svg class="story__chart" viewBox="-200 -190 400 200"><use href="#hours-fan"/></svg>
    <p class="story__total">20 Projects = 600 Hours<br>or 25% of Your Time Per Year...UGGH!</p>
    <p class="story__once">On-Boarding Once = <span class="accent">1.5%</span> of Your Time for<br>the entire year<span class="accent">...FOR REAL!</span></p>
  </div>

  <div class="solution">
    <h2 class="solution__title">A Better Solution:</h2>
    <p class="solution__subtitle">A Preventative Maintenance Program</p>
    <p class="solution__lead">You'll Have More Time to...</p>
    <div class="benefits">
      <div class="benefit"><div class="benefit__art" role="img" aria-label="Illustration of a hand holding a mobile phone"></div><p class="benefit__text">Focus on Communication with Your Team and Customers</p></div>
      <div class="benefit"><div class="benefit__art" role="img" aria-label="Illustration of a safety traffic cone"></div><p class="benefit__text">Focus on Safety to ensure it is a priority</p></div>
      <div class="benefit"><div class="benefit__art" role="img" aria-label="Illustration of turning gears"></div><p class="benefit__text">Focus on Productivity to ensure you meet all of your business unit's needs</p></div>
    </div>
    <h3 class="partner__title">You'll Have A Trusted Partner Who Provides…</h3>
    <ul class="pills"><li class="pill">Consistency</li><li class="pill">Predictability</li><li class="pill">Reliability</li></ul>
    <p class="aligned">Aligned with Your Needs</p>
    <ul class="features">
      <li>Safety Is Our #1 Objective</li>
      <li>Adapting to all of Your Scheduling Requirements</li>
      <li>A Single Point of Communication</li>
      <li>Integration w/ your Work Order Process &amp; Project Tracking</li>
      <li>A Dedicated Field Team, who Understands the Ins and Outs of Your Facility</li>
      <li>Rapid Response Time</li>
      <li>All Tasks and Jobs (Big or Small) Equally Prioritized</li>
      <li>Customized Billing and Future Budget Building</li>
      <li>Visual Facility Mapping</li>
    </ul>
  </div>
</section>

<!-- Landscape version -->
<section class="panel panel--wide">
  <div class="brand"><span class="brand__mark"></span>Verimbos</div>

  <div class="story">
    <h2 class="story__intro-title">Imagine What You Could Do with<br>An Extra 30% More Time Each Year?</h2>
    <p class="story__intro-text">Time that you wouldn't need to spend on-boarding a new company every time you have a project or facility upgrade.</p>
    <div class="story__hero" role="img" aria-label="Illustration of a worker in a hard hat thinking, with question marks"></div>
    <h1 class="story__headline">It Takes <span class="accent">30+ Hours</span> to Source and Onboard the Most Qualified Vendor...<span class="accent">YIKES!</span></h1>
    <svg class="story__chart" viewBox="-200 -190 400 200"><use href="#hours-fan"/></svg>
    <p class="story__total">20 Projects = 600 Hours<br>or 25% of Your Time Per Year...UGGH!</p>
    <p class="story__once">On-Boarding Once = <span class="accent">1.5%</span> of Your Time for<br>the entire year<span class="accent">...FOR REAL!</span></p>
  </div>

  <div class="solution">
    <h2 class="solution__title">A Better Solution:</h2>
    <p class="solution__subtitle">A Preventative Maintenance Program</p>
    <p class="solution__lead">You'll Have More Time to…</p>
    <div class="benefits">
      <div class="benefit"><div class="benefit__art" role="img" aria-label="Illustration of a hand holding a mobile phone"></div><p class="benefit__text">Focus on Communication with Your Team and Customers</p></div>
      <div class="benefit"><div class="benefit__art" role="img" aria-label="Illustration of a safety traffic cone"></div><p class="benefit__text">Focus on Safety to ensure it is a priority</p></div>
      <div class="benefit"><div class="benefit__art" role="img" aria-label="Illustration of turning gears"></div><p class="benefit__text">Focus on Productivity to ensure you meet all of your business unit's needs</p></div>
    </div>
    <h3 class="partner__title">You'll Have A Trusted Partner Who Provides…</h3>
    <ul class="pills"><li class="pill">Consistency</li><li class="pill">Predictability</li><li class="pill">Reliability</li></ul>
    <p class="aligned">Aligned with Your Needs</p>
    <div class="divider"></div>
    <ul class="features">
      <li>Safety Is Our #1 Objective</li>
      <li>Adapting to all of Your Scheduling Requirements</li>
      <li>A Single Point of Communication</li>
      <li>Integration w/ your Work Order Process &amp; Project Tracking</li>
      <li>A Dedicated Field Team, who Understands the Ins and Outs of Your Facility</li>
      <li>Rapid Response Time</li>
      <li>All Tasks and Jobs (Big or Small) Equally Prioritized</li>
      <li>Customized Billing and Future Budget Building</li>
      <li>Visual Facility Mapping</li>
    </ul>
  </div>
</section>

<!-- Shared chart: onboarding hours per step -->
<svg width="0" height="0" style="position:absolute" aria-hidden="true">
  <defs>
    <g id="hours-fan">
      <path d="M0 0 L-120 0 A120 120 0 0 1 -110.87 -45.92 Z" fill="#1a2ba3"/>
      <path d="M0 0 L-166.3 -68.89 A180 180 0 0 1 -127.28 -127.28 Z" fill="#9cc81a"/>
      <path d="M0 0 L-70.71 -70.71 A100 100 0 0 1 -38.27 -92.39 Z" fill="#1a2ba3"/>
      <path d="M0 0 L-45.92 -110.87 A120 120 0 0 1 0 -120 Z" fill="#9cc81a"/>
      <path d="M0 0 L0 -80 A80 80 0 0 1 30.62 -73.91 Z" fill="#1a2ba3"/>
      <path d="M0 0 L45.92 -110.87 A120 120 0 0 1 84.85 -84.85 Z" fill="#9cc81a"/>
      <path d="M0 0 L70.71 -70.71 A100 100 0 0 1 92.39 -38.27 Z" fill="#1a2ba3"/>
      <path d="M0 0 L92.39 -38.27 A100 100 0 0 1 100 0 Z" fill="#9cc81a"/>
      <path d="M-60 0 A60 60 0 0 1 60 0 Z" fill="#ffffff" opacity=".22"/>
      <path d="M-110 0 A110 110 0 0 1 110 0" fill="none" stroke="#ffffff" stroke-opacity=".25" stroke-width="14"/>
      <text class="chart-value" x="-94" y="-13" text-anchor="middle">4</text>
      <text class="chart-value" x="-120" y="-74" text-anchor="middle">7</text>
      <text class="chart-value" x="-44" y="-61" text-anchor="middle">3</text>
      <text class="chart-value" x="-19" y="-88" text-anchor="middle">4</text>
      <text class="chart-value" x="12" y="-57" text-anchor="middle">2</text>
      <text class="chart-value" x="53" y="-74" text-anchor="middle">4</text>
      <text class="chart-value" x="67" y="-38" text-anchor="middle">3</text>
      <text class="chart-value" x="78" y="-10" text-anchor="middle">3</text>
      <rect x="-20" y="-11" width="40" height="18" rx="9" fill="#ffffff"/>
      <text class="chart-label" x="0" y="2" text-anchor="middle">Hours</text>
      <text class="chart-label" x="-178" y="-40" text-anchor="middle"><tspan x="-178">Source</tspan><tspan x="-178" dy="8">Vendors &amp;</tspan><tspan x="-178" dy="8">Bidders</tspan></text>
      <text class="chart-label" x="-166" y="-168" text-anchor="middle"><tspan x="-166">Schedule and</tspan><tspan x="-166" dy="8">Completing a</tspan><tspan x="-166" dy="8">Walkthrough</tspan></text>
      <text class="chart-label" x="-56" y="-140" text-anchor="middle"><tspan x="-56">Reviewing</tspan><tspan x="-56" dy="8">Estimates</tspan></text>
      <text class="chart-label" x="-6" y="-182" text-anchor="middle"><tspan x="-6">Phone calls</tspan><tspan x="-6" dy="8">to clarify scope</tspan><tspan x="-6" dy="8">and any</tspan><tspan x="-6" dy="8">big revisions</tspan></text>
      <text class="chart-label" x="68" y="-172" text-anchor="middle"><tspan x="68">Present to</tspan><tspan x="68" dy="8">Decision</tspan><tspan x="68" dy="8">Maker &amp;</tspan><tspan x="68" dy="8">Financing</tspan><tspan x="68" dy="8">Approval</tspan></text>
      <text class="chart-label" x="150" y="-116" text-anchor="middle"><tspan x="150">Negotiations</tspan><tspan x="150" dy="8">with Vendor</tspan></text>
      <text class="chart-label" x="158" y="-68" text-anchor="middle"><tspan x="158">Awarding &amp;</tspan><tspan x="158" dy="8">Purchasing</tspan></text>
      <text class="chart-label" x="172" y="-30" text-anchor="middle"><tspan x="172">Completing</tspan><tspan x="172" dy="8">On-Boarding</tspan><tspan x="172" dy="8">Paperwork</tspan></text>
    </g>
  </defs>
</svg>

</body>
</html>
```